Classy, Elegant, Simple Business Card Design

Looking to have a classy, simple, and elegant design. Want a top notch designed business card. I really like the look of the new brivo credit card. I also like the design I attached. I am trying to reach 21-29 year old females for booking us for there wedding or event. We offer Disc Jockey Service, Photo Booth Rentals, and Uplighting .

Target Market(s)

21-28 year old females

Contact Information for Business Card

Has to have logo, website, email, and phone number

Font styles to use
Other font styles liked:
• open to font choice, modern, clean
Designer to choose
33a6d7
0791cd
0555a3
ffffff

Requirements
Must have
• Has to have logo, website, email, and phone number
Nice to have
• I really like the design of the new brivo credit card. I also included my logo and some designs I like
Should not have
• clutter or too much info

```html
<!DOCTYPE html>
<html lang="en">
<head>
<meta charset="utf-8">
<title>Bellmere Events – Business Card</title>
<link rel="stylesheet" href="https://fonts.googleapis.com/css2?family=Montserrat:wght@400;500;700&family=Questrial&display=swap">
<style>
  :root {
    --sky: #33a6d7;
    --azure: #0791cd;
    --royal: #0555a3;
    --navy: #14305e;
    --white: #ffffff;
    --stage: #e6e7e9;
    --ink-soft: #6b6f75;
    --card-shadow: 0 10px 28px rgba(0, 0, 0, 0.14);
  }
  * { margin: 0; padding: 0; box-sizing: border-box; }
  html, body {
    width: 1200px;
    height: 1200px;
    overflow: hidden;
    background: var(--stage);
  }
  .canvas {
    position: relative;
    width: 1200px;
    height: 1200px;
  }
  .card {
    position: absolute;
    left: 266px;
    width: 668px;
    height: 390px;
    background: var(--white);
    box-shadow: var(--card-shadow);
  }
  .card--front { top: 150px; }
  .card--back { top: 662px; }

  .brand {
    font-family: "Montserrat", sans-serif;
    font-weight: 500;
    color: var(--royal);
    letter-spacing: 0.06em;
    white-space: nowrap;
    display: flex;
    align-items: center;
    gap: 14px;
  }
  .brand__dot {
    width: 14px;
    height: 14px;
    border-radius: 50%;
    background: var(--azure);
    flex: none;
  }
  .card--front .brand {
    position: absolute;
    left: 0;
    right: 0;
    top: 160px;
    justify-content: center;
    font-size: 50px;
  }
  .card--back .brand {
    position: absolute;
    left: 48px;
    top: 112px;
    font-size: 36px;
  }

  .holder {
    position: absolute;
    left: 48px;
    top: 200px;
    font-family: "Montserrat", sans-serif;
    font-size: 24px;
    letter-spacing: 0.02em;
    color: var(--royal);
    white-space: nowrap;
  }
  .holder__last { font-weight: 700; }

  .divider {
    position: absolute;
    left: 49px;
    top: 247px;
    width: 574px;
    height: 2px;
    background: linear-gradient(90deg, var(--royal), var(--azure));
  }

  .contacts {
    position: absolute;
    left: 52px;
    top: 263px;
    list-style: none;
    font-family: "Questrial", sans-serif;
    font-size: 17.5px;
    color: var(--ink-soft);
    letter-spacing: 0.03em;
  }
  .contacts__item {
    display: flex;
    align-items: center;
    height: 26px;
  }
  .contacts__icon {
    width: 18px;
    height: 18px;
    margin-right: 9px;
    flex: none;
  }
</style>
</head>
<body>
<main class="canvas">
  <section class="card card--front" aria-label="Card front">
    <div class="brand"><span class="brand__dot"></span>BELLMERE EVENTS</div>
  </section>

  <section class="card card--back" aria-label="Card back">
    <div class="brand"><span class="brand__dot"></span>BELLMERE EVENTS</div>

    <p class="holder">DANIEL <span class="holder__last">HARWICK</span></p>
    <div class="divider"></div>

    <ul class="contacts">
      <li class="contacts__item">
        <svg class="contacts__icon" viewBox="0 0 18 18" aria-hidden="true">
          <rect x="5" y="1" width="8" height="16" rx="1.5" fill="none" stroke="#0791cd" stroke-width="1.5"/>
          <circle cx="9" cy="14" r="1" fill="#0791cd"/>
        </svg>
        123 456 7890
      </li>
      <li class="contacts__item">
        <svg class="contacts__icon" viewBox="0 0 18 18" aria-hidden="true">
          <rect x="1.5" y="4" width="15" height="10" fill="#0791cd"/>
          <path d="M1.5 4 L9 10 L16.5 4" fill="none" stroke="#fff" stroke-width="1.3"/>
        </svg>
        hello@bellmereevents.com
      </li>
      <li class="contacts__item">
        <svg class="contacts__icon" viewBox="0 0 18 18" aria-hidden="true">
          <circle cx="9" cy="9" r="7.5" fill="none" stroke="#0791cd" stroke-width="1.4"/>
          <ellipse cx="9" cy="9" rx="3.2" ry="7.5" fill="none" stroke="#0791cd" stroke-width="1.1"/>
          <line x1="1.5" y1="9" x2="16.5" y2="9" stroke="#0791cd" stroke-width="1.1"/>
        </svg>
        www.bellmereevents.com
      </li>
      <li class="contacts__item">
        <svg class="contacts__icon" viewBox="0 0 18 18" aria-hidden="true">
          <path d="M9 17 C9 17 3 10.5 3 7 A6 6 0 0 1 15 7 C15 10.5 9 17 9 17 Z" fill="#0791cd"/>
          <circle cx="9" cy="7" r="2.2" fill="#fff"/>
        </svg>
        Suit 123, City, Country, Postal Code
      </li>
    </ul>
  </section>
</main>
</body>
</html>
```